Business card por a urban DJ, up scale audience target

Need a sober design, modern, conservative colors but i can consider some options, y play rnb, hip hop, EDM and top40.

Business card for contact and personal info, double sided, use logo attrached please; im 42 so i need a card acording to my age an target audience.

Target Market(s)

Adult people, up scale audience

Industry/Entity Type

Music Download

Contact Information for Business Card

Cel (318) 5024471963 www.kelvarodun.com

Requirements
Must have
• open mind
Nice to have
• open mind
Should not have
• DJ

```html
<!DOCTYPE html>
<html lang="en">
<head>
<meta charset="utf-8">
<title>Kelva Business Card</title>
<link rel="stylesheet" href="https://fonts.googleapis.com/css2?family=Open+Sans:wght@400;600;700;800&display=swap">
<style>
  :root {
    --backdrop: #2b2b2b;
    --card: #ffffff;
    --ink: #2a2a2a;
    --ink-soft: #3a3a3a;
    --ghost: #d9d9d9;
  }
  * { margin: 0; padding: 0; box-sizing: border-box; }
  html, body {
    width: 1200px; height: 1189px; overflow: hidden;
    background: var(--backdrop);
    font-family: "Open Sans", sans-serif;
    color: var(--ink);
  }
  .sheet {
    width: 1200px; height: 1189px;
    display: flex; flex-direction: column; align-items: center; justify-content: center;
    gap: 48px;
  }
  .card {
    position: relative;
    width: 960px; height: 540px;
    background: var(--card);
    overflow: hidden;
  }

  /* Back side */
  .card-back .ghost-name {
    position: absolute; left: 0; right: 0; top: 110px;
    text-align: center;
    font-size: 250px; font-weight: 800; letter-spacing: -6px;
    color: var(--ghost); line-height: 1;
  }
  .card-back .brand-name {
    position: absolute; left: 0; right: 0; top: 185px;
    text-align: center;
    font-size: 120px; font-weight: 800; letter-spacing: 2px;
    color: var(--ink); line-height: 1;
  }
  .card-back .site {
    position: absolute; right: 120px; bottom: 70px;
    font-size: 26px; font-weight: 600; color: var(--ink-soft);
  }

  /* Front side */
  .card-front .brand-name {
    position: absolute; left: 0; right: 0; top: 70px;
    text-align: center;
    font-size: 110px; font-weight: 800; letter-spacing: 2px;
    color: var(--ink); line-height: 1;
  }
  .card-front .details {
    position: absolute; left: 0; right: 0; top: 320px;
    display: flex; justify-content: center; align-items: stretch; gap: 34px;
  }
  .identity { text-align: right; }
  .identity .person {
    font-size: 34px; font-weight: 700; color: var(--ink-soft); margin-bottom: 8px;
  }
  .identity .address {
    font-size: 26px; font-weight: 700; color: var(--ink-soft); line-height: 1.3;
  }
  .divider { width: 3px; background: var(--ink); }
  .contacts { list-style: none; display: flex; flex-direction: column; gap: 6px; padding-top: 4px; }
  .contacts li {
    display: flex; align-items: center; gap: 12px;
    font-size: 27px; font-weight: 600; color: var(--ink-soft);
  }
  .contacts svg { width: 22px; height: 22px; fill: var(--ink-soft); flex: none; }
</style>
</head>
<body>
<main class="sheet">
  <section class="card card-back" aria-label="Card back">
    <div class="ghost-name" aria-hidden="true">KELVA</div>
    <div class="brand-name">KELVA</div>
    <div class="site">www.kelvarodun.com</div>
  </section>

  <section class="card card-front" aria-label="Card front">
    <div class="brand-name">KELVA</div>
    <div class="details">
      <div class="identity">
        <p class="person">Employee Name</p>
        <p class="address">Your Adress Inc 2nd Lane<br>Ave Edison, NJ 00000</p>
      </div>
      <div class="divider"></div>
      <ul class="contacts">
        <li>
          <svg viewBox="0 0 24 24" aria-hidden="true"><path d="M7 1h10a2 2 0 0 1 2 2v18a2 2 0 0 1-2 2H7a2 2 0 0 1-2-2V3a2 2 0 0 1 2-2zm0 3v9h10V4H7zm1 11v2h2v-2H8zm3 0v2h2v-2h-2zm3 0v2h2v-2h-2zm-6 3v2h2v-2H8zm3 0v2h2v-2h-2zm3 0v2h2v-2h-2z"/></svg>
          (318) 5024471963
        </li>
        <li>
          <svg viewBox="0 0 24 24" aria-hidden="true"><path d="M2 5h20v14H2V5zm2 2v.5l8 6 8-6V7H4zm0 3v7h16v-7l-8 6-8-6z"/></svg>
          info@youremail.com
        </li>
        <li>
          <svg viewBox="0 0 24 24" aria-hidden="true"><circle cx="12" cy="12" r="10"/><path d="M8 7c2 0 3 1 3 2s-2 1-2 3 2 2 2 4M15 6c-1 1 0 2 1 3s2 1 3 0" stroke="#fff" stroke-width="1.6" fill="none"/></svg>
          www.kelvarodun.com
        </li>
      </ul>
    </div>
  </section>
</main>
</body>
</html>
```